TRV Business Card

Business card design for a handyman company. Want to portray a professional image and stay away from the "Mom & Pops" image that is normally associated with handyman companies.

Business

```html
<!DOCTYPE html>
<html lang="en">
<head>
<meta charset="utf-8">
<title>TRV Business Card</title>
<link href="https://fonts.googleapis.com/css2?family=Audiowide&display=swap" rel="stylesheet">
<style>
  :root {
    --page-bg: #ffffff;
    --card-blue: #0a8fcd;
    --ink-dark: #1d1d1f;
    --ink-light: #ffffff;
    --accent-orange: #e08a12;
  }
  html, body {
    margin: 0;
    padding: 0;
    width: 1200px;
    height: 999px;
    overflow: hidden;
    background: var(--page-bg);
  }
  .canvas {
    position: relative;
    width: 1200px;
    height: 999px;
    font-family: "Audiowide", sans-serif;
  }
  .card {
    position: absolute;
    left: 111px;
    top: 196px;
    width: 1011px;
    height: 552px;
    background: var(--card-blue);
  }
  .company-title {
    position: absolute;
    left: 0;
    right: 0;
    top: 40px;
    margin: 0;
    text-align: center;
    font-size: 47px;
    font-weight: 400;
    letter-spacing: 1px;
    color: var(--ink-dark);
    text-transform: uppercase;
  }
  .brand-mark {
    position: absolute;
    left: 386px;
    top: 128px;
    width: 294px;
    height: 294px;
    display: flex;
    align-items: center;
    justify-content: center;
    gap: 16px;
  }
  .brand-mark .mark-dot {
    width: 26px;
    height: 26px;
    background: var(--accent-orange);
    border-radius: 50%;
  }
  .brand-mark .mark-name {
    font-size: 86px;
    color: var(--ink-dark);
    line-height: 1;
  }
  .info-block {
    position: absolute;
    margin: 0;
    padding: 0;
    list-style: none;
    color: var(--ink-light);
    font-size: 21px;
    line-height: 30px;
    text-transform: uppercase;
  }
  .services { left: 32px; top: 406px; }
  .contact { right: 32px; top: 406px; text-align: center; }
  .email {
    position: absolute;
    left: 0;
    right: 0;
    top: 432px;
    margin-left: -26px;
    text-align: center;
    color: var(--ink-light);
    font-size: 17px;
    text-transform: uppercase;
  }
</style>
</head>
<body>
<div class="canvas">
  <section class="card">
    <h1 class="company-title">Total Repair Ventures</h1>

    <div class="brand-mark" role="img" aria-label="TRV company logo">
      <span class="mark-dot"></span>
      <span class="mark-name">TRV</span>
    </div>

    <ul class="info-block services">
      <li>Home Repairs</li>
      <li>Handyman Services</li>
      <li>Drain Cleaning</li>
      <li>Carpet Cleaning</li>
    </ul>

    <p class="email">info@trvhomeservices.com</p>

    <ul class="info-block contact">
      <li>2750 W Prairie Ave</li>
      <li>Salina, KS 67401</li>
      <li>(555) 246-7081 P</li>
      <li>(555) 266-3920 F</li>
    </ul>
  </section>
</div>
</body>
</html>
```